Halvorne apparel business card

We are a clothing manufacturers agent based in London. Our clients are fashion retailers in the UK and Europe. We are looking for a business card design that communicates corporate stability and a creative edge

Target Market(s)

our customers are large international fashion retailers, smaller fashion stores and distributors and designers

Industry/Entity Type

Clothing

```html
<!DOCTYPE html>
<html lang="en">
<head>
<meta charset="utf-8">
<title>Halvorne Apparel – Business Card</title>
<link href="https://fonts.googleapis.com/css2?family=Tinos:wght@400;700&family=Arimo:wght@400&display=swap" rel="stylesheet">
<style>
  :root {
    --backdrop: #e4e2de;
    --card: #fbfbfb;
    --card-shade: #ececec;
    --ink: #111111;
    --ink-soft: #333333;
    --rule: #8a8a8a;
    --band: #141414;
    --band-text: #f4f4f4;
  }
  * { margin: 0; padding: 0; box-sizing: border-box; }
  html, body {
    width: 1200px; height: 818px; overflow: hidden;
    background: var(--backdrop);
  }
  .card {
    position: absolute; left: 150px; top: 152px;
    width: 900px; height: 514px;
    background: linear-gradient(160deg, var(--card) 0%, var(--card) 55%, var(--card-shade) 100%);
    box-shadow: 0 10px 30px rgba(0,0,0,.18);
    overflow: hidden;
  }
  .company {
    position: absolute; left: 0; top: 0; width: 430px; height: 424px;
    display: flex; flex-direction: column; align-items: center; justify-content: center;
    font-family: "Tinos", "Times New Roman", serif; font-weight: 700;
    font-size: 34px; letter-spacing: 1px; color: var(--ink);
    text-align: center; line-height: 1.12; text-transform: uppercase;
  }
  .divider {
    position: absolute; left: 432px; top: 70px; width: 1px; height: 290px;
    background: var(--rule);
  }
  .contact {
    position: absolute; left: 500px; top: 92px;
    font-family: "Arimo", "Helvetica Neue", Arial, sans-serif; color: var(--ink-soft);
  }
  .contact__name {
    font-family: "Tinos", "Times New Roman", serif; font-weight: 700;
    font-size: 28px; color: var(--ink); line-height: 1;
  }
  .contact__role { font-size: 17px; margin-top: 4px; margin-bottom: 46px; }
  .contact__list { list-style: none; }
  .contact__item {
    display: flex; align-items: center; gap: 14px;
    font-size: 21px; margin-bottom: 10px; color: var(--ink);
  }
  .contact__icon { width: 18px; height: 18px; flex: none; }
  .address-band {
    position: absolute; left: 0; bottom: 0; width: 100%; height: 90px;
    background: var(--band);
    display: flex; align-items: center; justify-content: center;
    font-family: "Arimo", "Helvetica Neue", Arial, sans-serif;
    font-size: 26px; color: var(--band-text); letter-spacing: .3px;
  }
</style>
</head>
<body>
  <div class="card">
    <div class="company">
      <span>Halvorne Apparel</span>
      <span>Ltd</span>
    </div>
    <div class="divider"></div>
    <div class="contact">
      <div class="contact__name">Employee Name</div>
      <div class="contact__role">Managing Director</div>
      <ul class="contact__list">
        <li class="contact__item">
          <svg class="contact__icon" viewBox="0 0 18 18" aria-hidden="true">
            <circle cx="9" cy="5" r="4" fill="#111"/>
            <path d="M1 18 C1 11 17 11 17 18 Z" fill="#111"/>
          </svg>
          0012 3456 789
        </li>
        <li class="contact__item">
          <svg class="contact__icon" viewBox="0 0 18 18" aria-hidden="true">
            <rect x="0" y="2" width="18" height="14" fill="#111"/>
            <path d="M1 3 L9 10 L17 3 M1 15 L7 9 M17 15 L11 9" stroke="#fff" stroke-width="1.4" fill="none"/>
          </svg>
          info@youremail.com
        </li>
        <li class="contact__item">
          <svg class="contact__icon" viewBox="0 0 18 18" aria-hidden="true">
            <circle cx="9" cy="9" r="8.5" fill="#111"/>
            <ellipse cx="9" cy="9" rx="3.5" ry="8" stroke="#fff" stroke-width="1.1" fill="none"/>
            <path d="M1 9 H17 M2.5 5 H15.5 M2.5 13 H15.5" stroke="#fff" stroke-width="1.1"/>
          </svg>
          www.yourwebsite.com
        </li>
      </ul>
    </div>
    <div class="address-band">Your Adress Inc 2nd Lane, Ave Edison, NJ 00000</div>
  </div>
</body>
</html>
```